We are looking to recreate our Harlow & Partners Jobsite Sign. This sign will be placed by the street at each of our jobsites. We want to keep this sign simple, but at the same time, want to add a catching appeal to the design for anyone passing by. We want to stick to a two color scheme (Harlow Blue, and White). Please only use the Company Logo that I have uploaded for this project. Please also see a mock up of what we would like to include on this sign. The Sign Dimensions will be 4' x 8'. Please keep all verbiage uniform with the verbiage on the sample design I have uploaded. LET YOUR CREATIVITY FLOW!

```html
<!DOCTYPE html>
<html lang="en">
<head>
<meta charset="utf-8">
<title>Harlow &amp; Partners Jobsite Sign</title>
<link rel="stylesheet" href="https://fonts.googleapis.com/css2?family=Merriweather:wght@400;700;900&display=swap">
<style>
  :root {
    --harlow-blue: #2c3190;
    --white: #ffffff;
    --backdrop: #8f8f8f;
  }
  * { margin: 0; padding: 0; box-sizing: border-box; }
  html, body { width: 983px; height: 1200px; overflow: hidden; }
  body {
    background: var(--backdrop);
    font-family: "Merriweather", Georgia, serif;
    position: relative;
  }
  .sign {
    position: absolute;
    left: 38px; top: 374px;
    width: 908px; height: 452px;
    background: var(--white);
  }
  .sign__panel {
    position: absolute;
    left: 20px; top: 19px;
    width: 868px; height: 321px;
    background: var(--harlow-blue);
    color: var(--white);
  }
  .sign__rail { position: absolute; background: var(--harlow-blue); }
  .sign__rail--left  { left: 0; top: 340px; width: 20px; height: 112px; }
  .sign__rail--right { right: 0; top: 340px; width: 20px; height: 112px; }
  .sign__rail--base  { left: 0; bottom: 0; width: 908px; height: 18px; }

  .license { position: absolute; left: 22px; top: 26px; }
  .license__label { font-size: 10px; font-weight: 700; display: block; }
  .license__number { font-size: 25px; font-weight: 700; letter-spacing: 0.5px; display: block; margin-top: 1px; }

  .location {
    position: absolute; left: 0; width: 100%; top: 24px;
    text-align: center; font-size: 33px; font-weight: 900;
  }
  .social { position: absolute; right: 22px; top: 36px; display: flex; gap: 6px; }
  .social__dot { width: 25px; height: 25px; border-radius: 50%; background: var(--white); }

  .brand {
    position: absolute; left: 60px; top: 96px; width: 330px;
    text-align: right; line-height: 1;
  }
  .brand__name { font-size: 70px; font-weight: 700; letter-spacing: -1px; display: block; }
  .brand__sub { font-size: 31px; font-weight: 700; display: block; margin-top: 4px; }
  .divider {
    position: absolute; left: 416px; top: 100px;
    width: 3px; height: 112px; background: var(--white);
  }
  .trade {
    position: absolute; left: 440px; top: 100px; width: 330px;
    text-align: center; font-size: 49px; font-weight: 700; line-height: 1.05;
  }
  .tagline {
    position: absolute; left: 0; width: 100%; top: 222px;
    text-align: center; font-size: 44px; font-weight: 700;
  }
  .tagline sup { font-size: 20px; vertical-align: 18px; font-weight: 400; }

  .contact {
    position: absolute; left: 20px; top: 340px; width: 868px; height: 94px;
    display: flex; align-items: center; justify-content: space-around;
    color: var(--harlow-blue);
  }
  .contact__item { display: flex; align-items: center; gap: 8px; font-weight: 900; }
  .contact__item--web { font-size: 30px; }
  .contact__item--phone { font-size: 34px; }
</style>
</head>
<body>
  <div class="sign">
    <div class="sign__panel">
      <div class="license">
        <span class="license__label">License Number:</span>
        <span class="license__number">CGC4827315</span>
      </div>
      <div class="location">Maple Grove, Florida</div>
      <div class="social" aria-label="Social media">
        <span class="social__dot"></span>
        <span class="social__dot"></span>
        <span class="social__dot"></span>
      </div>
      <div class="brand">
        <span class="brand__name">Harlow</span>
        <span class="brand__sub">&amp; Partners, Inc.</span>
      </div>
      <div class="divider"></div>
      <div class="trade">General<br>Contractors</div>
      <div class="tagline">“We Build Lasting Trust”<sup>®</sup></div>
    </div>
    <div class="sign__rail sign__rail--left"></div>
    <div class="sign__rail sign__rail--right"></div>
    <div class="sign__rail sign__rail--base"></div>
    <div class="contact">
      <div class="contact__item contact__item--web">
        <svg width="26" height="26" viewBox="0 0 26 26" aria-hidden="true">
          <g fill="none" stroke="currentColor" stroke-width="2">
            <circle cx="13" cy="13" r="11"/>
            <ellipse cx="13" cy="13" rx="5" ry="11"/>
            <line x1="2" y1="13" x2="24" y2="13"/>
            <line x1="13" y1="2" x2="13" y2="24"/>
            <path d="M4 7.5h18M4 18.5h18"/>
          </g>
        </svg>
        <span>HarlowPartners.net</span>
      </div>
      <div class="contact__item contact__item--phone">
        <svg width="30" height="30" viewBox="0 0 24 24" aria-hidden="true">
          <path fill="currentColor" d="M6.6 10.8a15.1 15.1 0 0 0 6.6 6.6l2.2-2.2a1 1 0 0 1 1-.25 11.4 11.4 0 0 0 3.6.57 1 1 0 0 1 1 1V20a1 1 0 0 1-1 1A17 17 0 0 1 3 4a1 1 0 0 1 1-1h3.5a1 1 0 0 1 1 1c0 1.25.2 2.45.57 3.57a1 1 0 0 1-.25 1z"/>
        </svg>
        <span>555-201-4478</span>
      </div>
    </div>
  </div>
</body>
</html>
```